Banner for homepage

It is a new banner for the homepage, temporary site address is 61.187.40.72 ( is the biggest banner only ) . Would be 5 variations for image content as below (in Portuguese ) :

Image 1:
Leitor de codigo de barras
Todos os tipos de leitores de código de barras para as mais diversas aplicações.
( example of product images in : http://www.quentorlabs.com/en-US/Pages/Category.aspx?category=barcode-scanners&cat=KLT)

Image 2:
Impressora de etiquetas
Identifique o que for nessário com o melhor custo/beneficio e flexibilidade de materiais de impressão.
( example of product images in : vintor.com in label printers desktop and industrial)

Image 3:
Impressora de cupom
Imprima recibos e cupons fiscais com agilidade e qualidade, temos a impressora certa para o seu PDV.
( example of product images in : http://www.palutrek.com.br/equipamento-categoria-impressoras+fiscais.html)

Image 4:
Coletor de dados
Computadores móveis com leitor de código de barras, que levam a automação para frente de trabalho.
( example of product images in : http://www.quentorlabs.com/en-US/Pages/Category.aspx?cat=KLT&category=hand-held-mobile-computer)

Image 5:
Etiquetas e Ribbons:
Etiquetas adesivas e não adesivas em vários de tipos de materiais, papéis e plásticos. O ribbon certo para impressão perfeita em cada material.
( example of product images in : http://www.tagmirelo.com/cats/supplies/barcode-printer.htm?nav=hdr)

```html
<!DOCTYPE html>
<html lang="pt-BR">
<head>
<meta charset="utf-8">
<title>TAGPOINT – Soluções em Automação e Código de barras</title>
<link rel="stylesheet" href="https://fonts.googleapis.com/css2?family=Oswald:wght@400;500;600&family=Ubuntu:wght@500;700&family=Arimo:wght@400;700&display=swap">
<style>
:root{
  --red:#cf3a3f;
  --red-dark:#b52a30;
  --page:#ececec;
  --nav-top:#4a4a4a;
  --nav-bottom:#2e2e2e;
  --ink:#333;
  --white:#fff;
  --orange:#e8581c;
  --gold-1:#ffe45a;
  --gold-2:#f2a900;
  --sky-1:#9fcbe8;
  --sky-2:#e8f3fb;
  --strip:rgba(120,170,215,.55);
  --brown-1:#3a302a;
  --brown-2:#5a4a3e;
  --taupe:#8b7f78;
}
*{box-sizing:border-box;margin:0;padding:0}
html,body{width:1200px;height:569px;overflow:hidden}
body{background:var(--page);font-family:Arimo,Arial,sans-serif;color:var(--ink);position:relative}
.site-header{position:absolute;left:0;top:0;width:1200px;height:104px;background:linear-gradient(var(--red),var(--red-dark))}
.brand{position:absolute;left:104px;top:8px;font-family:Oswald,sans-serif;font-weight:600;font-size:36px;letter-spacing:4px;color:var(--white);line-height:46px}
.tagline{position:absolute;left:118px;top:58px;font-size:13px;color:var(--white)}
.top-links{position:absolute;right:107px;top:9px;display:flex;font-size:12px;font-weight:700;color:var(--white)}
.top-links span{padding:0 11px;border-left:1px solid rgba(255,255,255,.6)}
.top-links span:first-child{border:none}
.top-links span:last-child{padding-right:0}
.contact-box{position:absolute;top:35px;height:47px;background:var(--white);border-radius:2px;padding:5px 11px;font-family:Oswald,sans-serif;box-shadow:0 1px 2px rgba(0,0,0,.25)}
.contact-box strong{display:block;font-weight:500;font-size:15px;color:#333;line-height:19px}
.contact-box small{display:block;font-size:11px;color:var(--orange);line-height:16px}
.chat{left:824px;width:111px}
.phones{left:952px;width:143px}
.phones svg{position:absolute;right:9px;top:20px}
.main-nav{position:absolute;left:75px;top:93px;width:1042px;height:42px;background:linear-gradient(var(--nav-top),var(--nav-bottom));border-radius:3px;display:flex;align-items:center;font-family:Oswald,sans-serif;font-size:13px;color:var(--white);box-shadow:0 2px 3px rgba(0,0,0,.3)}
.main-nav span{padding:0 11px;height:42px;line-height:42px;border-right:1px solid #222;box-shadow:1px 0 0 #555}
.search{position:absolute;left:879px;top:9px;width:153px;height:24px;background:#2a2a2a;border:1px solid #1c1c1c;border-radius:3px;font-family:Arimo,sans-serif;font-size:12px;color:#aaa;line-height:22px;padding-left:9px}
.search svg{position:absolute;right:6px;top:5px}
.hero{position:absolute;left:97px;top:157px;width:742px;height:339px;border-radius:5px;overflow:hidden;background:linear-gradient(var(--sky-1),var(--sky-2) 70%)}
.hero-title{height:54px;background:linear-gradient(#555,#2b2b2b);text-align:center;font-family:Oswald,sans-serif;font-weight:500;font-size:39px;line-height:54px;color:var(--gold-2)}
.hero-title span{background:linear-gradient(var(--gold-1),var(--gold-2));-webkit-background-clip:text;background-clip:text;color:transparent}
.hero-strip{position:absolute;left:0;top:89px;width:520px;height:99px;background:var(--strip)}
.hero-band{position:absolute;left:0;top:257px;width:742px;height:82px;background:linear-gradient(#d8353c,#b8272d)}
.hero-product{position:absolute;left:500px;top:87px;width:242px;height:240px;background:linear-gradient(135deg,#5a5e66,#c9cbcf 55%,#eceded);border-radius:6px 6px 0 0}
.hero-text{position:absolute;z-index:2;left:21px;top:90px;width:470px;font-family:Ubuntu,sans-serif;font-weight:700;font-size:27px;line-height:31px;color:var(--white);text-shadow:0 0 3px #1d4f85,0 2px 2px #1d4f85}
.cta{position:absolute;z-index:2;left:76px;top:273px;width:209px;height:48px;border-radius:24px;background:linear-gradient(#ffe34d,#f2a800);border:2px solid #c98a00;font-family:Arimo,sans-serif;font-weight:700;font-size:31px;color:#333;text-align:center;line-height:43px}
.promo{position:absolute;left:864px;width:234px;border-radius:4px;overflow:hidden;color:var(--white)}
.promo-fast{top:158px;height:162px;background:linear-gradient(135deg,var(--brown-1),var(--brown-2))}
.promo-invoice{top:336px;height:160px;background:linear-gradient(135deg,#9d928b,var(--taupe))}
.promo h3{position:absolute;z-index:2;left:24px;top:16px;font-family:Oswald,sans-serif;font-weight:500;font-size:29px;line-height:36px;white-space:nowrap}
.promo-fast h3{color:#d9b98a}
.promo-invoice h3{color:#3a3a3a}
.promo h3 b{color:var(--white);font-weight:500}
.promo p{position:absolute;z-index:2;left:24px;top:60px;width:150px;font-size:13px;line-height:18px}
.promo-invoice p{left:30px;top:63px;width:130px}
.promo-img{position:absolute;right:0;bottom:0;width:92px;height:90px}
.promo-fast .promo-img{background:linear-gradient(135deg,#e38a3a,#9c4e1c)}
.promo-invoice .promo-img{width:82px;height:84px;background:linear-gradient(135deg,#1d4a52,#0c1e22)}
.read-more{position:absolute;z-index:2;left:24px;top:112px;width:92px;height:23px;border-radius:12px;font-family:Oswald,sans-serif;font-size:13px;text-align:center;line-height:23px}
.promo-fast .read-more{background:linear-gradient(#f0d7aa,#c49a5c);color:#5a3a1c}
.promo-invoice .read-more{left:30px;top:112px;background:linear-gradient(#ef5050,#b81f24);color:var(--white)}
.section-title{position:absolute;left:107px;top:529px;font-family:Oswald,sans-serif;font-weight:500;font-size:19px;color:#444}
.section-rule{position:absolute;left:97px;top:563px;width:1020px;height:2px;background:#dcdcdc}
</style>
</head>
<body>
<header class="site-header">
  <div class="brand">TAGPOINT</div>
  <div class="tagline">Soluções em Automação e Código de barras</div>
  <nav class="top-links"><span>Principal</span><span>Quem Somos</span><span>Entre em Contato</span></nav>
  <div class="contact-box chat"><strong>CHAT ONLINE</strong><small>CLIQUE AQUI</small></div>
  <div class="contact-box phones"><strong>TELEFONES</strong><small>TODOS OS ESTADOS</small>
    <svg width="9" height="6" viewBox="0 0 9 6"><path d="M0 0h9L4.5 6z" fill="#333"/></svg></div>
</header>

<nav class="main-nav">
  <span>LEITOR DE CÓDIGO DE BARRAS</span>
  <span>IMPRESSORA DE ETIQUETAS</span>
  <span>AUTOMAÇÃO COMERCIAL</span>
  <span>ETIQUETAS</span>
  <span>COLETOR DE DADOS</span>
  <span>IMPRESSORA DE CARTÃO</span>
  <span>MARCAS</span>
  <div class="search">Busca
    <svg width="13" height="13" viewBox="0 0 13 13"><circle cx="5" cy="5" r="3.8" fill="none" stroke="#ddd" stroke-width="1.8"/><path d="M8 8l4 4" stroke="#ddd" stroke-width="2"/></svg></div>
</nav>

<section class="hero">
  <h1 class="hero-title"><span>LEITOR DE CÓDIGO DE BARRAS</span></h1>
  <div class="hero-band"></div>
  <div class="hero-strip"></div>
  <div class="hero-product" role="img" aria-label="Leitor de código de barras de balcão"></div>
  <p class="hero-text">Todos os tipos de leitores de código de barras para as mais diversas aplicações.</p>
  <div class="cta">Veja Mais</div>
</section>

<aside class="promo promo-fast">
  <div class="promo-img" role="img" aria-label="Caixa de papelão para entrega"></div>
  <h3>Entrega<b>Rápida</b></h3>
  <p>Enviamos sua compra para todo o Brasil.</p>
  <div class="read-more">Leia Mais</div>
</aside>

<aside class="promo promo-invoice">
  <div class="promo-img" role="img" aria-label="Sacola de compras"></div>
  <h3>Boleto<b>Faturado</b></h3>
  <p>Receba seu pedido com os boletos.</p>
  <div class="read-more">Leia Mais</div>
</aside>

<h2 class="section-title">DESTAQUES</h2>
<div class="section-rule"></div>
</body>
</html>
```